Plakat für Hersteller von maßgefertigten Tischunikaten aus Massivholz
Zielgruppe
Wir sind einen Firma die sich auf die Fertigung von maßgefertigten Tischunikaten aus Massivholz spezialisiert hat. Unsere Zielgruppe sind Design affine Leute, im Alter von 35-55 Jahren
Aufgabenstellung
Wir benötigen das Design für eine Messewand mit den Maßen 443X227 cm. 5 Zentimeter rundlaufen dürfen keine Elemente mehr platziert werden. Die Messewand steht im Hintergrund von unserem Stand bei verschiedenen Designmessen
Infos die auf die Messewand müssen: Logo, Tischmanufaktur aus Stuttgart, Maßgefertigte Tischunikate (Bei der Formulierung bin ich flexibel, ihr könnt bspw. auch nur Stichworte benutzen, aber Stuttgart und maßgefertigt ist wichtig).
Die Messewand soll sehr minimalistisch gestaltet sein, bei der letzten Messewand hatten wir ein Foto von einem Tisch im Hintergrund und das sah merkwürdig aus.

```html
<!DOCTYPE html>
<html lang="de">
<head>
<meta charset="utf-8">
<title>Holmgart Manufaktur – Messewand</title>
<link rel="stylesheet" href="https://fonts.googleapis.com/css2?family=Montserrat:wght@200;300&family=Jost:wght@700&display=swap">
<style>
  :root {
    --page-bg: #e4e4e4;
    --wall-dark: #232323;
    --wall-mid: #2c2c2c;
    --wall-light: #575757;
    --ink: #ffffff;
  }
  * { margin: 0; padding: 0; box-sizing: border-box; }
  html, body {
    width: 1200px;
    height: 816px;
    overflow: hidden;
    background: var(--page-bg);
  }
  .trade-wall {
    position: absolute;
    left: 20px;
    top: 110px;
    width: 1160px;
    height: 595px;
    background:
      radial-gradient(circle at 0 0, var(--wall-light) 0%, var(--wall-mid) 32%, var(--wall-dark) 62%);
    color: var(--ink);
    font-family: "Montserrat", sans-serif;
  }
  .headline {
    position: absolute;
    left: 64px;
    top: 70px;
    font-weight: 200;
    font-size: 66px;
    line-height: 79.4px;
    letter-spacing: 0;
    text-transform: uppercase;
    white-space: nowrap;
  }
  .headline .city {
    font-family: "Jost", sans-serif;
    font-weight: 700;
    font-size: 70px;
    letter-spacing: -0.5px;
  }
  .brand {
    position: absolute;
    right: 70px;
    top: 108px;
    display: flex;
    align-items: center;
    gap: 12px;
  }
  .brand-dot {
    width: 34px;
    height: 34px;
    border: 3px solid var(--ink);
    border-radius: 50%;
  }
  .brand-name {
    font-weight: 300;
    font-size: 22px;
    letter-spacing: 3px;
    text-transform: uppercase;
  }
  .footer-rule {
    position: absolute;
    left: 0;
    top: 527px;
    width: 776px;
    height: 1px;
    background: var(--ink);
  }
  .web-address {
    position: absolute;
    right: 70px;
    top: 518px;
    font-weight: 300;
    font-size: 14.5px;
    letter-spacing: 0.6px;
    text-transform: uppercase;
  }
</style>
</head>
<body>
  <section class="trade-wall">
    <h1 class="headline">
      Jeder Tisch<br>
      wurde persön-<br>
      lich in <span class="city">Stuttgart</span><br>
      hergestellt und<br>
      gefertigt.
    </h1>
    <div class="brand">
      <span class="brand-dot"></span>
      <span class="brand-name">Holmgart</span>
    </div>
    <div class="footer-rule"></div>
    <p class="web-address">www.holmgart-manufaktur.de</p>
  </section>
</body>
</html>
```